High-end construction company needs a business card design

We need a modern looking business card that draws people in, is memorable and looks so good people will want to sick it on their fridges.
On the first side what is needed are:
Logo
My name - Tomas Brevik
Title - Managing Director
Website - www.kelvora.co.uk
Email - tomas@kelvora.co.uk
Telephone - 020 4917 2365
Mobile - 07845139072
On the back side was is needed is a list of all the services we provide:
-Kitchen Renovations
-Bathroom Renovations
-House Renovations
-Garage Conversions
-Extensions
-Loft Conversions
-Conservatories
-Carpentry
-Tiling
-Electrical
-Plumbing & Heating
-Bricklaying
-Landscaping
-Decorating
-Plastering
We would like the colours to be the same shades as on the logo with grey or black for the words.
Target Market(s)
Anyone who needs building work done
Contact Information for Business Card
This business card is for a construction company which strives to deliver excellent service and quality.
The look and feel of the card should represent this.
Requirements
Must have
- On the first side what is needed are:
Logo
My name - Tomas Brevik
Title - Managing Director
Website - www.kelvora.co.uk
Email - tomas@kelvora.co.uk
Telephone - 020 4917 2365
Mobile - 07845139072
Nice to have
- Cool looking features

```html
<!DOCTYPE html>
<html lang="en">
<head>
<meta charset="utf-8">
<title>Kelvora Construction Ltd — Business Card</title>
<link rel="stylesheet" href="https://fonts.googleapis.com/css2?family=Open+Sans:wght@400;600;800&display=swap">
<style>
  :root {
    --bg: #dedede;
    --green-dark: #4a8f3f;
    --green-mid: #5aa445;
    --green-light: #78c143;
    --green-faint: #559a48;
    --white: #ffffff;
    --shadow: rgba(0,0,0,0.22);
  }
  * { margin: 0; padding: 0; box-sizing: border-box; }
  html, body {
    width: 1200px; height: 810px; overflow: hidden;
    background: var(--bg);
    font-family: "Open Sans", Arial, sans-serif;
  }
  .stage { position: relative; width: 1200px; height: 810px; }

  .card { position: absolute; box-shadow: 0 10px 28px var(--shadow); overflow: hidden; }

  /* Front */
  .card-front { left: 90px; top: 105px; width: 360px; height: 600px; background: var(--white); }
  .front-band { position: absolute; inset: 0; }
  .front-brand {
    position: absolute; left: 0; right: 0; top: 110px; text-align: center;
    color: var(--green-light); font-weight: 800; line-height: 1.05;
  }
  .front-brand .brand-name { display: block; font-size: 46px; letter-spacing: 2px; }
  .front-brand .brand-sub { display: block; font-size: 13px; letter-spacing: 3px; margin-top: 6px; }

  .machine-art {
    position: absolute; left: 226px; top: 262px; width: 116px; height: 176px;
    border-radius: 6px;
    background: linear-gradient(160deg, var(--green-light) 0%, var(--green-mid) 100%);
  }

  .person { position: absolute; left: 28px; top: 372px; }
  .person-name { color: var(--green-light); font-weight: 800; font-size: 20px; text-transform: uppercase; }
  .person-title { color: var(--white); font-size: 14px; margin-top: 2px; }

  .divider { position: absolute; left: 28px; right: 28px; top: 450px; display: flex; align-items: center; gap: 8px; }
  .divider-line { flex: 1; height: 1px; background: var(--green-light); }
  .icon { width: 20px; height: 20px; border-radius: 50%; background: var(--green-light); display: flex; align-items: center; justify-content: center; }
  .icon svg { width: 12px; height: 12px; }

  .contact { position: absolute; left: 28px; right: 20px; top: 484px; color: var(--white); font-size: 13px; line-height: 1.9; }
  .contact .sep { color: var(--green-light); margin: 0 5px; }

  /* Back */
  .card-back { left: 510px; top: 225px; width: 600px; height: 360px; background: var(--green-dark); }
  .back-brand {
    position: absolute; left: 0; right: 0; top: 48px; text-align: center;
    color: var(--green-faint); font-weight: 800; line-height: 1.05;
  }
  .back-brand .brand-name { display: block; font-size: 48px; letter-spacing: 3px; }
  .back-brand .brand-sub { display: block; font-size: 14px; letter-spacing: 4px; margin-top: 4px; }

  .services { position: absolute; list-style: none; color: var(--white); font-size: 15px; line-height: 1.45; }
  .services li { display: flex; align-items: center; gap: 10px; }
  .services li::before {
    content: ""; width: 0; height: 0;
    border-top: 5px solid transparent; border-bottom: 5px solid transparent;
    border-left: 9px solid var(--green-light);
  }
  .services-a { left: 40px; top: 218px; }
  .services-b { left: 240px; top: 188px; }
  .services-c { left: 420px; top: 158px; }
</style>
</head>
<body>
<main class="stage">

  <section class="card card-front" aria-label="Business card front">
    <svg class="front-band" width="360" height="600" viewBox="0 0 360 600" aria-hidden="true">
      <polygon points="0,330 360,255 360,600 0,600" fill="var(--green-dark)"/>
    </svg>

    <div class="machine-art" role="img" aria-label="Excavator arm and bucket illustration"></div>

    <div class="front-brand">
      <span class="brand-name">KELVORA</span>
      <span class="brand-sub">CONSTRUCTION LTD</span>
    </div>

    <div class="person">
      <div class="person-name">Tomas Brevik</div>
      <div class="person-title">Managing Director</div>
    </div>

    <div class="divider">
      <span class="divider-line"></span>
      <span class="icon" aria-label="Telephone"><svg viewBox="0 0 12 12"><path d="M3 1 L5 3 L4 4.5 Q5 7 7.5 8 L9 7 L11 9 L9.5 11 Q3 10 1 2.5 Z" fill="var(--green-dark)"/></svg></span>
      <span class="icon" aria-label="Mobile"><svg viewBox="0 0 12 12"><rect x="3.5" y="1" width="5" height="10" rx="1" fill="none" stroke="var(--green-dark)" stroke-width="1.3"/></svg></span>
      <span class="icon" aria-label="Email"><svg viewBox="0 0 12 12"><rect x="1.5" y="3" width="9" height="6" fill="none" stroke="var(--green-dark)" stroke-width="1.2"/><path d="M1.5 3 L6 6.5 L10.5 3" fill="none" stroke="var(--green-dark)" stroke-width="1.2"/></svg></span>
      <span class="icon" aria-label="Website"><svg viewBox="0 0 12 12"><circle cx="6" cy="6" r="4.5" fill="none" stroke="var(--green-dark)" stroke-width="1.2"/><path d="M1.5 6 H10.5 M6 1.5 Q3.5 6 6 10.5 M6 1.5 Q8.5 6 6 10.5" fill="none" stroke="var(--green-dark)" stroke-width="1"/></svg></span>
      <span class="divider-line"></span>
    </div>

    <div class="contact">
      <div>020 4917 2365<span class="sep">|</span>07845139072</div>
      <div>tomas@kelvora.co.uk<span class="sep">|</span>www.kelvora.co.uk</div>
    </div>
  </section>

  <section class="card card-back" aria-label="Business card back">
    <div class="back-brand">
      <span class="brand-name">KELVORA</span>
      <span class="brand-sub">CONSTRUCTION LTD</span>
    </div>

    <ul class="services services-a">
      <li>Kitchen Renovations</li>
      <li>Bathroom Renovations</li>
      <li>House Renovations</li>
      <li>Garage Conversions</li>
      <li>Extensions</li>
    </ul>
    <ul class="services services-b">
      <li>Plumbing &amp; Heating</li>
      <li>Bricklaying</li>
      <li>Landscaping</li>
      <li>Decorating</li>
      <li>Plastering</li>
    </ul>
    <ul class="services services-c">
      <li>Loft Conversions</li>
      <li>Conservatories</li>
      <li>Carpentry</li>
      <li>Tiling</li>
      <li>Electrical</li>
    </ul>
  </section>

</main>
</body>
</html>
```